Networking card

I just need a simple design with the following information:
Ravin Doshu
318.647.2094
rdoshu583016@mailvanta.com

I would like to have a white background with blue text like in this sample: https://cardmintly.com/business-card-207346/

```html
<!DOCTYPE html>
<html lang="en">
<head>
<meta charset="utf-8">
<title>Ravin Doshu – Networking Card</title>
<link rel="stylesheet" href="https://fonts.googleapis.com/css2?family=Montserrat:wght@500;800&display=swap">
<style>
  :root {
    --navy: #02395c;
    --ink-grey: #7a7a7a;
    --paper: #ffffff;
    --backdrop: #dedede;
  }
  * { margin: 0; padding: 0; box-sizing: border-box; }
  html, body {
    width: 1200px;
    height: 1200px;
    overflow: hidden;
    background: var(--backdrop);
    font-family: "Montserrat", Arial, sans-serif;
  }
  .card {
    position: absolute;
    left: 179px;
    width: 861px;
    height: 496px;
  }
  .card-front {
    top: 84px;
    background: var(--navy);
    display: flex;
    align-items: center;
    justify-content: center;
  }
  .front-name {
    color: var(--paper);
    font-weight: 800;
    font-size: 69px;
    letter-spacing: 0.01em;
    margin-top: -12px;
  }
  .card-back {
    top: 621px;
    background: var(--paper);
    overflow: hidden;
  }
  .back-name {
    position: absolute;
    left: 48px;
    top: 28px;
    color: var(--navy);
    font-weight: 800;
    font-size: 68px;
    line-height: 1;
    letter-spacing: 0.02em;
  }
  .back-title {
    position: absolute;
    left: 49px;
    top: 115px;
    color: var(--ink-grey);
    font-weight: 500;
    font-size: 45px;
    line-height: 1;
    letter-spacing: 0.03em;
  }
  .title-rule {
    position: absolute;
    left: 53px;
    top: 175px;
    width: 104px;
    height: 2px;
    background: var(--navy);
  }
  .contact-row {
    position: absolute;
    left: 47px;
    display: flex;
    align-items: center;
  }
  .contact-row.phone { top: 337px; }
  .contact-row.email { top: 401px; }
  .contact-icon {
    width: 38px;
    height: 38px;
    flex: none;
    display: block;
  }
  .contact-text {
    color: var(--ink-grey);
    font-weight: 500;
    font-size: 37px;
    line-height: 1;
    letter-spacing: 0.12em;
  }
  .phone .contact-text { margin-left: 22px; }
  .email .contact-text { margin-left: 18px; letter-spacing: 0.09em; }
  .base-band {
    position: absolute;
    left: 0;
    bottom: 0;
    width: 100%;
    height: 19px;
    background: var(--navy);
  }
</style>
</head>
<body>
  <section class="card card-front">
    <h1 class="front-name">Ravin Doshu</h1>
  </section>

  <section class="card card-back">
    <h2 class="back-name">Ravin Doshu</h2>
    <p class="back-title">Founder</p>
    <div class="title-rule"></div>

    <div class="contact-row phone">
      <svg class="contact-icon" viewBox="0 0 38 38" aria-hidden="true">
        <rect width="38" height="38" fill="#02395c"/>
        <path d="M14 9c-3 2-4 6-2 11s5 8 9 9c2 1 4 0 5-1l-3-4-2 1c-2-1-4-4-5-7l1-2-3-7z" fill="#ffffff"/>
      </svg>
      <span class="contact-text">318.647.2094</span>
    </div>

    <div class="contact-row email">
      <svg class="contact-icon" viewBox="0 0 38 38" aria-hidden="true">
        <rect width="38" height="38" fill="#02395c"/>
        <rect x="6" y="11" width="26" height="17" fill="none" stroke="#ffffff" stroke-width="2"/>
        <path d="M6 11l13 10 13-10M6 28l10-9M32 28l-10-9" fill="none" stroke="#ffffff" stroke-width="1.6"/>
      </svg>
      <span class="contact-text">rdoshu583016@mailvanta.com</span>
    </div>

    <div class="base-band"></div>
  </section>
</body>
</html>
```